Refer a Friend A5 Flyer for Healthcare Staff

We need an A5 flyer that we can hand out to existing and new staff members promoting our Refer a friend Scheme. We need the leaflet to encourage staff to talk to their family and friends about joining our Healthcare Agency, which provides staff to local care related establishments. Using our logo and brand colours blue and green, as per our website, the final design will need to clearly convey the benefits and attractions of referring additional staff to the team. In addition is the promotion of our our Socials page, requesting staff to like the page and to like and share various posts.

Target Market(s)

Healthcare and potential Healthcare Staff

Industry/Entity Type

Healthcare

Colors
33b8a4
3277b5

Requirements
Must have
• Company Logo, Brand colours,
• text; "Refer a Friend and receive a £50 Bonus after just 1 completed shift"
• text; "3 easy steps to refer a friend, 1 Fill out your name on the back of your Business Card 2 Hand the card to your friend or any person you wish to refer, 3 ask your friend to present the card to us when they attend their interview"
• text; "Like and share any of our Open Days on our Socials for a chance to win a prize, you can find us easily by searching @CarewellPlacementGroup"
• text; "Like our Page to stay up to date with our events and offers"
Nice to have
• care worker / elderly care / support worker pictures
• Content / pics from website www.carewellplacementgroup.co.uk

```html
<!DOCTYPE html>
<html lang="en">
<head>
<meta charset="utf-8">
<title>Carewell Placement – Refer a Friend Flyer</title>
<link rel="stylesheet" href="https://fonts.googleapis.com/css2?family=Poppins:wght@400;600;800&family=Bebas+Neue&family=Roboto+Condensed:wght@400;700&family=Great+Vibes&display=swap">
<style>
  :root {
    --brand-blue: #1256a6;
    --brand-teal: #2bb39e;
    --ink-grey: #7a7a7a;
    --paper: #ffffff;
    --backdrop: #ece9e4;
  }
  * { box-sizing: border-box; margin: 0; padding: 0; }
  html, body { width: 1099px; height: 1200px; overflow: hidden; background: var(--backdrop); }
  .flyer {
    position: absolute; left: 135px; top: 12px;
    width: 828px; height: 1175px;
    background: var(--paper);
    overflow: hidden;
    box-shadow: 0 4px 14px rgba(0,0,0,.18);
  }
  .flyer svg.decor { position: absolute; left: 0; top: 0; }
  .brand {
    position: absolute; left: 52px; top: 222px;
    display: flex; align-items: center; gap: 14px;
  }
  .brand__mark { width: 22px; height: 22px; border-radius: 50%; background: var(--brand-blue); }
  .brand__name {
    font: 400 40px/1.05 "Poppins", sans-serif; color: var(--brand-blue);
  }
  .brand__tagline {
    position: absolute; left: 260px; top: 318px;
    font: 400 15px "Poppins", sans-serif; color: var(--ink-grey);
  }
  .offer {
    position: absolute; left: 59px; top: 401px; width: 711px; height: 250px;
    background: var(--brand-blue); border-radius: 20px; color: #fff;
    padding: 14px 26px 0;
    font-family: "Poppins", sans-serif; text-align: center;
  }
  .offer__lead { font-weight: 600; font-size: 39px; line-height: 56px; border-bottom: 1.5px solid rgba(255,255,255,.8); }
  .offer__amount { font-weight: 800; font-size: 110px; line-height: 110px; letter-spacing: -2px; border-bottom: 1.5px solid rgba(255,255,255,.8); }
  .offer__terms { font-weight: 600; font-size: 38.5px; line-height: 60px; }
  .team-photo {
    position: absolute; left: 60px; top: 678px; width: 162px; height: 172px;
    background: linear-gradient(180deg, #dfe9f0, #c7d8e6 60%, #f3f6f8);
    border-radius: 6px;
  }
  .steps { position: absolute; left: 252px; top: 682px; width: 530px; }
  .steps__title { font: 400 48px/1 "Bebas Neue", sans-serif; color: var(--brand-blue); letter-spacing: .5px; margin-bottom: 8px; }
  .steps__list { list-style: none; font: 400 21px/1.2 "Roboto Condensed", sans-serif; color: var(--brand-teal); }
  .steps__list li { display: flex; gap: 6px; margin-bottom: 5px; white-space: nowrap; }
  .steps__list b { color: var(--brand-blue); font-weight: 700; }
  .social {
    position: absolute; left: 59px; top: 873px; width: 711px; height: 137px;
    background: var(--brand-teal); border-radius: 20px;
    display: flex; align-items: center; justify-content: center; text-align: center;
    font: 400 25.5px/30px "Poppins", sans-serif; color: #fff;
  }
  .social strong { font-weight: 800; }
  .signoff {
    position: absolute; left: 0; width: 828px; top: 1026px; text-align: center;
    font: 400 40px/1 "Great Vibes", cursive; color: var(--brand-blue);
  }
</style>
</head>
<body>
<main class="flyer">
  <svg class="decor" width="828" height="1175" viewBox="0 0 828 1175">
    <defs>
      <linearGradient id="gardenTones" x1="0" y1="0" x2="1" y2="1">
        <stop offset="0" stop-color="#5f7d3a"/>
        <stop offset=".55" stop-color="#8fa865"/>
        <stop offset="1" stop-color="#b9cde6"/>
      </linearGradient>
    </defs>
    <path role="img" aria-label="Photo of a smiling carer with an elderly man in a wheelchair in a sunny garden"
      d="M110,0 L828,0 L828,312 C790,350 720,372 660,362 C560,345 495,275 420,172 C330,62 220,8 110,0Z"
      fill="url(#gardenTones)"/>
    <path d="M0,28 C180,12 320,60 420,178 C495,280 560,352 660,368 C720,378 790,356 828,318" fill="none" stroke="#2bb39e" stroke-width="9"/>
    <path d="M0,0 L110,0 C220,8 330,62 420,172 L418,180 C320,60 180,14 0,30Z" fill="#1256a6"/>
    <path d="M0,1122 C160,1080 320,1108 500,1148 C650,1170 760,1150 828,1128" fill="none" stroke="#2bb39e" stroke-width="8"/>
    <path d="M0,1135 C160,1098 320,1120 500,1158 C650,1178 760,1160 828,1140 L828,1175 L0,1175Z" fill="#1256a6"/>
  </svg>

  <div class="brand">
    <span class="brand__mark"></span>
    <span class="brand__name">Carewell<br>Placement</span>
  </div>
  <div class="brand__tagline">Care Made Easy</div>

  <section class="offer">
    <p class="offer__lead">REFER A FRIEND AND RECEIVE A</p>
    <p class="offer__amount">£50 BONUS</p>
    <p class="offer__terms">AFTER JUST 1 COMPLETED SHIFT</p>
  </section>

  <div class="team-photo" role="img" aria-label="Photo of a group of care staff in light blue uniforms joining hands"></div>

  <section class="steps">
    <h2 class="steps__title">3 Easy Steps to Refer a Friend</h2>
    <ol class="steps__list">
      <li><b>1.</b><span>Fill out your name on the back of your Business Card</span></li>
      <li><b>2.</b><span>Hand the card to your friend or any person you wish to refer</span></li>
      <li><b>3.</b><span>ask your friend to present the card to us when they<br>attend their interview</span></li>
    </ol>
  </section>

  <section class="social">
    <p>Like &amp; share any of our Open Days on <strong>our Socials</strong><br>for a chance to win a prize, you can find us easily<br>by searching <strong>@CarewellPlacementGroup</strong></p>
  </section>

  <p class="signoff">Like our Page to stay up to date with our events and offers</p>
</main>
</body>
</html>
```